Need A Business Card Design For An Automobile Detailing Business

I need a business card design for an automobile detailing service.

On the front of the card it should have the following information:
The logo,
OWNER NAME
Company LLC

We specialize in:
- paint protection
- paint correction
- Head light Restoration
- Vinyl, Leather and plastic Restoration

Phone Number

On the back it should have the image of the attached car and the logo designed how you think it would look best.

The color that should be used are black, red, yellow, and white. Background would most likely look best in black with information in white and titles in either red or yellow.

Could lead to more work in the future for the winner.

EDIT: WHEN SUBMITTING ENTRIES PLEASE DO NO SUBMIT MOCKUPS. ONLY FLAT IMAGES. IT'S HARD TO SEE YOUR DESIGNS CLEARLY WHEN THEY ARE ON A MOCKUP.

```html
<!DOCTYPE html>
<html lang="en">
<head>
<meta charset="UTF-8">
<title>Crimson Crest Restoration – Business Card</title>
<link href="https://fonts.googleapis.com/css2?family=Lato:wght@400;700;900&display=swap" rel="stylesheet">
<style>
  :root {
    --page-bg: #3a3a3c;
    --card-black: #0b0b0b;
    --accent-red: #e3222a;
    --text-white: #ffffff;
    --chrome-light: #d9dadc;
    --chrome-dark: #4a4b4f;
  }
  * { box-sizing: border-box; margin: 0; padding: 0; }
  html, body {
    width: 1200px; height: 900px; overflow: hidden;
    background: var(--page-bg);
    font-family: "Lato", Arial, sans-serif;
  }
  .canvas { position: relative; width: 1200px; height: 900px; }

  .card {
    position: absolute;
    width: 560px; height: 320px;
    background: var(--card-black);
    border-radius: 26px;
    overflow: hidden;
    box-shadow: 0 18px 40px rgba(0,0,0,.45);
  }
  .card--back { left: 70px; top: 90px; }
  .card--front { left: 570px; top: 490px; }

  .brand {
    position: absolute; right: 28px; top: 24px;
    display: flex; align-items: center; gap: 8px;
    color: var(--accent-red);
    font-weight: 900; font-size: 19px; letter-spacing: .5px;
    text-transform: uppercase;
  }
  .brand__mark { width: 14px; height: 14px; background: var(--accent-red); }

  .car-visual {
    position: absolute; left: 190px; top: 110px;
    width: 180px; height: 100px; border-radius: 40px;
    background: radial-gradient(ellipse at center, var(--chrome-light) 0%, var(--chrome-dark) 55%, var(--card-black) 80%);
  }

  .divider {
    position: absolute; right: 0; top: 70px;
    width: 300px; height: 2px; background: var(--accent-red);
  }
  .side-tab {
    position: absolute; left: 0; top: 92px;
    width: 8px; height: 30px; background: var(--accent-red);
  }
  .person { position: absolute; left: 36px; top: 88px; }
  .person__name { color: var(--text-white); font-size: 24px; font-weight: 400; }
  .person__role { color: var(--accent-red); font-size: 17px; margin-top: 2px; }

  .phone {
    position: absolute; left: 36px; top: 160px;
    display: flex; align-items: center; gap: 10px;
    color: var(--text-white); font-size: 18px; letter-spacing: .5px;
  }

  .services { position: absolute; left: 36px; top: 196px; right: 28px; }
  .services__title {
    display: flex; align-items: center; gap: 12px;
    color: var(--accent-red); font-weight: 700; font-size: 17px;
  }
  .services__title::after { content: ""; flex: 1; height: 2px; background: var(--accent-red); }
  .services__list { list-style: none; margin-top: 4px; }
  .services__item {
    display: flex; align-items: center; gap: 12px;
    color: var(--text-white); font-size: 15px; line-height: 21px;
  }
  .services__item::before {
    content: ""; width: 11px; height: 11px; border-radius: 50%;
    background: var(--accent-red);
  }
</style>
</head>
<body>
<main class="canvas">
  <section class="card card--back" aria-label="Card back">
    <div class="brand"><span class="brand__mark"></span>Crimson Crest Restoration</div>
    <div class="car-visual" role="img" aria-label="Chrome sports car with doors raised"></div>
  </section>

  <section class="card card--front" aria-label="Card front">
    <div class="brand"><span class="brand__mark"></span>Crimson Crest Restoration</div>
    <div class="divider"></div>
    <div class="side-tab"></div>
    <div class="person">
      <p class="person__name">Marco Reyes</p>
      <p class="person__role">President</p>
    </div>
    <div class="phone">
      <svg width="16" height="16" viewBox="0 0 24 24" aria-hidden="true">
        <path fill="#e3222a" d="M6.6 10.8a15.1 15.1 0 0 0 6.6 6.6l2.2-2.2a1 1 0 0 1 1-.25 11.4 11.4 0 0 0 3.6.57 1 1 0 0 1 1 1V20a1 1 0 0 1-1 1A17 17 0 0 1 3 4a1 1 0 0 1 1-1h3.5a1 1 0 0 1 1 1c0 1.25.2 2.45.57 3.57a1 1 0 0 1-.25 1z"/>
      </svg>
      <span>1-555-014-2290</span>
    </div>
    <div class="services">
      <p class="services__title">We specialize in:</p>
      <ul class="services__list">
        <li class="services__item">paint protection</li>
        <li class="services__item">paint correction</li>
        <li class="services__item">Head light Restoration</li>
        <li class="services__item">Vinyl, Leather and plastic Restoration</li>
      </ul>
    </div>
  </section>
</main>
</body>
</html>
```